Bramwell Business Cards

Logo files are included. Full "Bramwell" logo should be included on the back of the business card. The B symbol should be included on the front with the contact information.

Bramwell, LLC is the company name and we do commercial construction and real estate development consulting services. Look for a fairly simple card design utilizing our logo.

```html
<!DOCTYPE html>
<html lang="en">
<head>
<meta charset="utf-8">
<title>Bramwell Business Cards</title>
<link rel="stylesheet" href="https://fonts.googleapis.com/css2?family=Poppins:wght@400;500;600&display=swap">
<style>
  :root {
    --navy: #19384d;
    --gold: #e9ad20;
    --white: #ffffff;
    --ink: #19384d;
    --backdrop: #e6e6e6;
  }
  * { box-sizing: border-box; margin: 0; padding: 0; }
  html, body {
    width: 1200px;
    height: 1085px;
    overflow: hidden;
    background: var(--backdrop);
    font-family: "Poppins", sans-serif;
  }
  .card {
    position: absolute;
    left: 301px;
    width: 578px;
    height: 343px;
    overflow: hidden;
  }
  .card-front { top: 163px; background: var(--white); }
  .card-back { top: 542px; background: var(--navy); }

  .front-bands { position: absolute; inset: 0; }

  .holder { position: absolute; left: 37px; top: 38px; }
  .holder-name {
    color: var(--gold);
    font-weight: 600;
    font-size: 23px;
    line-height: 1.1;
    letter-spacing: 0.2px;
  }
  .holder-role {
    color: var(--ink);
    font-size: 17px;
    line-height: 1.2;
    word-spacing: 3px;
  }

  .contact-list {
    position: absolute;
    left: 37px;
    top: 160px;
    list-style: none;
    color: var(--white);
    font-size: 17px;
    line-height: 20.5px;
  }
  .contact-list li { display: flex; align-items: center; gap: 7px; }
  .icon { width: 15px; height: 15px; flex: none; }

  .address {
    position: absolute;
    left: 37px;
    top: 261px;
    display: flex;
    gap: 6px;
    color: var(--ink);
    font-size: 17px;
    line-height: 21px;
  }
  .address .icon { margin-top: 2px; width: 14px; height: 18px; }

  .front-brand {
    position: absolute;
    left: 343px;
    top: 96px;
    width: 186px;
    height: 186px;
    display: flex;
    align-items: center;
    justify-content: center;
    color: var(--navy);
    font-weight: 600;
    font-size: 24px;
  }

  .back-brand {
    position: absolute;
    inset: 0;
    display: flex;
    flex-direction: column;
    align-items: center;
  }
  .back-mark {
    margin-top: 88px;
    width: 112px;
    height: 112px;
    border: 4px solid var(--white);
    border-radius: 50%;
  }
  .back-name {
    margin-top: 4px;
    color: var(--white);
    font-weight: 500;
    font-size: 56px;
    line-height: 1.1;
    letter-spacing: 1px;
  }
</style>
</head>
<body>

<section class="card card-front" aria-label="Business card front">
  <svg class="front-bands" viewBox="0 0 578 343" aria-hidden="true">
    <rect x="0" y="136" width="420" height="109" fill="var(--navy)"/>
    <rect x="470" y="136" width="108" height="109" fill="var(--gold)"/>
    <circle cx="436" cy="189" r="93" fill="var(--white)"/>
  </svg>

  <div class="holder">
    <h1 class="holder-name">DELMAR QUINT</h1>
    <p class="holder-role">Managing Director</p>
  </div>

  <ul class="contact-list">
    <li>
      <svg class="icon" viewBox="0 0 16 16" aria-hidden="true"><path d="M3.5 1.5l2.5 3-1.5 1.6c.8 1.9 2.3 3.4 4.2 4.2L10.3 8.8l3 2.5-1.4 2.5C7 13.4 2.6 9 2.2 3.9z" fill="var(--gold)"/><path d="M9.5 2.5a4 4 0 0 1 4 4M9.5 0.8a5.7 5.7 0 0 1 5.7 5.7" stroke="var(--gold)" stroke-width="1.2" fill="none"/></svg>
      <span>044-987 654 321</span>
    </li>
    <li>
      <svg class="icon" viewBox="0 0 16 16" aria-hidden="true"><rect x="1" y="3.5" width="14" height="9.5" fill="var(--gold)"/><path d="M1 3.5l7 5.5 7-5.5" stroke="var(--navy)" stroke-width="1.2" fill="none"/></svg>
      <span>hello@bramwellco.net</span>
    </li>
    <li>
      <svg class="icon" viewBox="0 0 16 16" aria-hidden="true"><g stroke="var(--gold)" stroke-width="1.3" fill="none"><circle cx="8" cy="8" r="6.5"/><ellipse cx="8" cy="8" rx="3" ry="6.5"/><path d="M1.5 8h13M2.5 4.8h11M2.5 11.2h11"/></g></svg>
      <span>www.bramwellco.net</span>
    </li>
  </ul>

  <address class="address">
    <svg class="icon" viewBox="0 0 14 18" aria-hidden="true"><path d="M7 0.5a6 6 0 0 1 6 6c0 4.5-6 11-6 11s-6-6.5-6-11a6 6 0 0 1 6-6z" fill="var(--gold)"/><circle cx="7" cy="6.5" r="2.2" fill="var(--white)"/></svg>
    <span>48, Harlow Avenue<br>Westmere, 654321</span>
  </address>

  <div class="front-brand">Bramwell</div>
</section>

<section class="card card-back" aria-label="Business card back">
  <div class="back-brand">
    <div class="back-mark" aria-hidden="true"></div>
    <p class="back-name">BRAMWELL</p>
  </div>
</section>

</body>
</html>
```